KFZ-Gutachter Banner

Ziel des Banners:
Der Banner soll auf die Tätigkeit als Kfz-Sachverständiger aufmerksam machen. Er wird im Außenbereich eingesetzt und soll schon aus der Ferne verständlich und gut lesbar sein.

Gestaltung:
• Schlichtes, professionelles Design (keine überladene Gestaltung, ruhige Farbwahl – anlehnend an den Farben schwarz und Rot.
• Ein Bild wo sich zwei hochwertige Autos verunfallt befinden
• Großzügige Schriftgrößen – der Text muss auch aus 20–30 m Entfernung gut lesbar sein
• Klare Informationsstruktur

Inhalte (Text):
1. Überschrift / Hauptaussage (groß & auffällig):
Kfz-Sachverständiger
oder
Unfallgutachten vom Profi
2. Kurze Beschreibung (kleiner, aber lesbar):
• Unfallgutachten
• Fahrzeugbewertung
• Technische Beratung
3. Kontaktdaten (am wichtigsten – sehr gut sichtbar & lesbar):
• Telefonnummer (z. B. groß & fett)
• Website oder E-Mail
• Optional: Standort oder “auch mobil im Einsatz”

Bildelemente:
• Optional ein dezentes Symbol oder Icon (z. B. Auto, Lupe, Checkzeichen) – nur wenn es nicht vom Text ablenkt

Format:
• Querformat, je nach Platz vor Ort (z. B. 3 m x 1,5 m)

Ingenieurbüro Lorenz Vahle Ostlinger Str.14 58706 Menden www.pruefwerk-tz.de

• Man muss sofort erkennen, dass es sich um einen KFZ-Gutachter handelt.

```html
<!DOCTYPE html>
<html lang="de">
<head>
<meta charset="utf-8">
<title>Kfz-Sachverständiger Banner</title>
<link href="https://fonts.googleapis.com/css2?family=Michroma&family=Oswald:wght@500;600&family=Poppins:wght@400;600&display=swap" rel="stylesheet">
<style>
  :root {
    --backdrop: #4d4d4d;
    --black: #000000;
    --white: #ffffff;
    --red: #c0151b;
    --ink: #2b2b2b;
    --grey-text: #3a3a3a;
  }
  html, body {
    margin: 0;
    width: 1200px;
    height: 1200px;
    overflow: hidden;
    background: var(--backdrop);
  }
  .banner {
    position: absolute;
    left: 60px;
    top: 330px;
    width: 1080px;
    height: 540px;
    background: var(--white);
    overflow: hidden;
  }
  .headline-band {
    position: absolute;
    left: 0;
    top: 0;
    width: 1080px;
    height: 127px;
    background: var(--black);
  }
  .headline-band svg { display: block; }
  .headline {
    fill: var(--white);
    font-family: "Michroma", sans-serif;
    font-size: 54px;
    font-weight: 700;
  }
  .photo {
    position: absolute;
    left: 0;
    top: 127px;
    width: 1080px;
    height: 249px;
    background:
      linear-gradient(90deg, #0d0f12 0%, #1b1e22 22%, rgba(0,0,0,0) 26%, rgba(0,0,0,0) 74%, #8c9096 78%, #b9bcc0 90%, #a7aaae 100%),
      linear-gradient(180deg, #5d8a3a 0%, #7da54a 45%, #6f7270 52%, #5e6160 58%, #6b9a36 66%, #4f7f2a 100%);
  }
  .info-band {
    position: absolute;
    left: 0;
    top: 376px;
    width: 1080px;
    height: 164px;
  }
  .brand {
    position: absolute;
    left: 0;
    top: 24px;
    width: 260px;
    text-align: center;
    font-family: "Poppins", sans-serif;
    color: var(--grey-text);
  }
  .brand-mark {
    width: 44px;
    height: 44px;
    margin: 0 auto 10px;
    border: 2px solid var(--grey-text);
  }
  .brand-name {
    font-size: 17px;
    letter-spacing: 1.5px;
    line-height: 1.3;
    white-space: nowrap;
  }
  .brand-sub {
    font-size: 9px;
    letter-spacing: 1px;
    line-height: 1.5;
    white-space: nowrap;
  }
  .divider {
    position: absolute;
    top: 14px;
    width: 6px;
    height: 124px;
    background: var(--black);
  }
  .divider-left { left: 260px; }
  .divider-right { left: 664px; }
  .contact {
    position: absolute;
    left: 268px;
    top: 0;
    width: 394px;
    height: 164px;
  }
  .phone {
    fill: var(--red);
    font-family: "Oswald", sans-serif;
    font-weight: 600;
    font-size: 78px;
  }
  .web {
    fill: var(--ink);
    font-family: "Oswald", sans-serif;
    font-weight: 500;
    font-size: 46px;
  }
  .services {
    position: absolute;
    left: 692px;
    top: 22px;
    list-style: none;
    margin: 0;
    padding: 0;
    font-family: "Poppins", sans-serif;
    font-weight: 600;
    font-size: 31px;
    color: var(--ink);
    line-height: 39px;
    white-space: nowrap;
  }
  .services li::before {
    content: "• ";
    font-size: 24px;
    vertical-align: 3px;
  }
</style>
</head>
<body>
  <main class="banner">
    <header class="headline-band">
      <svg width="1080" height="127" viewBox="0 0 1080 127">
        <text class="headline" x="38" y="90" textLength="998" lengthAdjust="spacingAndGlyphs">KFZ-SACHVERSTÄNDIGER</text>
      </svg>
    </header>
    <div class="photo" role="img" aria-label="Foto: zwei verunfallte Autos, links ein schwarzes Heck, rechts eine silberne Front, vor grünem Hintergrund mit Straße"></div>
    <section class="info-band">
      <div class="brand">
        <div class="brand-mark"></div>
        <div class="brand-name">LORENZ VAHLE</div>
        <div class="brand-sub">KFZ-SACHVERSTÄNDIGER<br>INGENIEURBÜRO</div>
      </div>
      <div class="divider divider-left"></div>
      <svg class="contact" width="394" height="164" viewBox="0 0 394 164">
        <text class="phone" x="32" y="82" textLength="340" lengthAdjust="spacingAndGlyphs">12345 678900</text>
        <text class="web" x="35" y="132" textLength="337" lengthAdjust="spacingAndGlyphs">WWW.PRUEFWERK-TZ.DE</text>
      </svg>
      <div class="divider divider-right"></div>
      <ul class="services">
        <li>Unfallgutachten</li>
        <li>Fahrzeugbewertung</li>
        <li>Technische Beratung</li>
      </ul>
    </section>
  </main>
</body>
</html>
```